Wordpress Powered Website. Outstanding Design Required. Using Morvenix Theme

Designers will not need to create anything other than the home page but there are some design elements on the home page which also need to be factored in: 6 product place holders and 2-3 slides for a slideshow (with images I provide).

Designers will need to familiarise themselves with the Morvenix theme to make sure that their design will work within the theme.

The winning designer will set up all the pages and navigation in place. This includes social media icons, favicon, widgets, etc. In other words, the home page needs to be designed and coded and the other preset theme pages need to be organised in a way that we can start using the website on completion of the job.

Most of the designs I had last time were too colourful. This needs to be subtle not in your face.

Background to the business/website:
Tandrel Banners is a new Australian venture which will sell large format printed banners and other signage. The market is very competitive so it is important to stand out visually and to have a website which is clean, easy to navigate and easy to order. It will be a combination of online sales and assisted sales but all sales enquiries will come from the website.

As our business is focused on presentation it is vital to have excellent design.
Purchased theme is Morvenix. Only this theme is to be used.

1. A home page using all the preset features of the Morvenix theme - it will just be basically taking my wireframe and inputting it to the live theme.
2. A three slide slideshow, ideally with an edited video. The static image slides can be provided by me during the handover. Placeholder for now.
Similar to this one: http://thebrindlecraft.com.au/

Attached is the logo which must be utilised, although it could also sit on a dark background. There is our mascot as well which can be used but does not have to be included.

Target Market(s)

Primarily B2B (business to business)
Main industries will be Construction, Retail, Community, Events & Trade Shows

Industry/Entity Type

Printing

Coding

Coded - Design and coding required

Font styles to use
Sans Serif

Requirements
Must have
• Must have the design files made to web pages within the Wordpress environment.
Nice to have
• Clean design. Stand out from competitors based on design.
Should not have
• Should not look like any competitor

```html
<!DOCTYPE html>
<html lang="en">
<head>
<meta charset="utf-8">
<title>Tandrel Banners — Large Format Printed Banners</title>
<link href="https://fonts.googleapis.com/css2?family=Lato:wght@400;700;900&family=Open+Sans:wght@400;600;700&display=swap" rel="stylesheet">
<style>
:root{
  --ink:#222;
  --text:#444;
  --muted:#666;
  --topbar:#1d1d1d;
  --light:#f1f1f1;
  --blue:#1e6fd1;
  --blue-dark:#1557a8;
  --red:#e01b1b;
  --footer:#3b3b3b;
  --footer-text:#d8d8d8;
  --white:#fff;
}
*{margin:0;padding:0;box-sizing:border-box}
html,body{width:1200px;height:3429px;overflow:hidden}
body{font-family:"Lato",sans-serif;color:var(--text);background:var(--white);position:relative}
.abs{position:absolute}
.section-title{position:absolute;left:0;width:1200px;text-align:center;font:900 25px "Lato",sans-serif;color:var(--ink);letter-spacing:.5px}

/* top bar */
.topbar{left:0;top:0;width:1200px;height:36px;background:var(--topbar);color:var(--white);font:700 14px "Open Sans",sans-serif}
.social{display:flex;gap:12px;position:absolute;left:98px;top:11px}
.social span{width:13px;height:13px;border-radius:50%;background:var(--white);display:block}
.topbar .contact{position:absolute;right:98px;top:9px;display:flex;gap:26px;align-items:center}
.topbar .contact div{display:flex;gap:8px;align-items:center}

/* header */
.header{left:0;top:36px;width:1200px;height:83px;background:var(--white)}
.brand{position:absolute;left:98px;top:14px;font:900 34px/1 "Lato",sans-serif;color:var(--red);letter-spacing:.5px}
.brand small{display:block;font:900 14px "Lato",sans-serif;color:var(--ink);letter-spacing:3px;margin-top:3px;text-align:center}
.nav{position:absolute;right:98px;top:34px;display:flex;font:700 13px "Open Sans",sans-serif;color:var(--ink)}
.nav a{color:inherit;text-decoration:none;padding:0 36px;border-left:1px solid #ddd}
.nav a:first-child{border-left:0}
.nav a:last-child{padding-right:0}

/* hero */
.hero{left:0;top:119px;width:1200px;height:430px;background:linear-gradient(120deg,#3b3a2c,#7a6b2c 45%,#a98f2e 70%,#4a4434)}
.hero-shade{left:0;top:0;width:1200px;height:430px;background:linear-gradient(90deg,rgba(0,0,0,.45),rgba(0,0,0,.05))}
.hero h1{position:absolute;left:100px;top:148px;width:520px;font:700 25px/1.45 "Open Sans",sans-serif;color:var(--white)}
.hero .cta{position:absolute;left:100px;top:262px;width:150px;height:34px;background:#111;color:var(--white);font:700 13px/34px "Open Sans",sans-serif;text-align:center}
.dots{position:absolute;left:100px;top:394px;display:flex;gap:6px}
.dots span{width:13px;height:13px;border-radius:50%;border:2px solid var(--white)}
.dots span:first-child{background:var(--white)}
.bubble{position:absolute;border-radius:50%;border:4px solid var(--white)}
.bubble-badge{position:absolute;left:830px;top:165px;width:100px;height:100px;border-radius:50%;background:var(--white);font:900 15px/100px "Lato",sans-serif;color:var(--red);text-align:center}

/* products */
.tile{position:absolute;width:302px;height:203px;display:flex;align-items:center;justify-content:center;font:700 20px "Open Sans",sans-serif;color:var(--white);text-shadow:0 1px 3px rgba(0,0,0,.6)}

/* difference */
.difference{left:0;top:1154px;width:1200px;height:412px;background:var(--light)}
.feature{position:absolute;width:240px;text-align:center}
.feature .icon{width:110px;height:110px;border-radius:50%;background:var(--blue);margin:0 auto;display:flex;align-items:center;justify-content:center;box-shadow:0 3px 0 var(--blue-dark)}
.feature h3{font:700 15px "Open Sans",sans-serif;color:var(--ink);margin-top:20px}
.feature p{font:400 12.5px/1.6 "Open Sans",sans-serif;color:var(--muted);margin-top:26px;padding:0 14px}

/* about */
.about-title{position:absolute;left:0;top:1603px;width:1200px;text-align:center;font:900 25px "Lato",sans-serif;color:var(--ink)}
.about-title b{color:var(--red);font-weight:900;margin:0 6px}
.about-body{left:100px;top:1687px;width:680px;font:400 13px/1.6 "Open Sans",sans-serif;color:var(--text)}
.about-body h4{font:700 14px "Open Sans",sans-serif;color:var(--ink);margin-bottom:6px}
.about-body p+p{margin-top:16px}

/* work */
.work{left:0;top:2007px;width:1200px;height:530px;background:var(--light)}
.cell{position:absolute}
.cell-label{display:flex;align-items:center;justify-content:center;text-align:center;font:700 17px/1.3 "Open Sans",sans-serif;color:var(--white);background:rgba(30,30,30,.82)}

/* process */
.step{position:absolute;width:240px;text-align:center}
.step .ring{width:134px;height:134px;border-radius:50%;border:5px solid var(--red);background:radial-gradient(circle at 50% 40%,#5a5a5a,#2b2b2b);margin:0 auto;display:flex;align-items:center;justify-content:center;box-shadow:0 6px 8px rgba(0,0,0,.25)}
.step p{font:700 13px "Open Sans",sans-serif;color:var(--ink);margin-top:28px}
.connector{position:absolute;display:flex;gap:10px;align-items:center}
.connector span{border-radius:50%;background:#ccc}

/* quote */
.quote{left:0;top:2869px;width:1200px;height:281px;background:linear-gradient(100deg,#d9c3a0 0%,#e7c9b9 25%,#cdd6e4 50%,#e8c7c0 75%,#d6b993 100%)}
.quote h2{position:absolute;left:0;top:44px;width:1200px;text-align:center;font:700 24px "Lato",sans-serif;color:var(--white)}
.field{position:absolute;background:var(--white);font:400 11px "Open Sans",sans-serif;color:#777;padding:7px 10px;border:1px solid #e2e2e2}
.submit{position:absolute;left:549px;top:206px;width:100px;height:30px;background:var(--red);color:var(--white);font:700 15px/30px "Open Sans",sans-serif;text-align:center}

/* footer */
.footer{left:0;top:3150px;width:1200px;height:279px;background:var(--footer);color:var(--footer-text);font:400 12px "Open Sans",sans-serif}
.footer h5{font:700 15px "Open Sans",sans-serif;color:var(--white);letter-spacing:.5px}
.links{list-style:none;margin-top:20px;font:700 11.5px/2.1 "Open Sans",sans-serif;color:var(--white)}
.links li::before{content:"›";margin-right:8px;color:#999}
.c-row{display:flex;gap:14px;margin-top:20px;line-height:1.45}
.c-row svg{flex:none}
.support-box{display:flex;align-items:center;gap:12px;width:196px;height:54px;border:1px solid #555;background:#333;margin-top:16px;padding:0 12px}
.support-box b{display:block;font:italic 700 16px "Open Sans",sans-serif;color:var(--white)}
.support-box i{font-size:11.5px;color:#bbb}
.foot-brand{position:absolute;left:903px;top:42px;font:900 34px/1 "Lato",sans-serif;color:#cfcfcf}
.foot-brand small{display:block;font:900 12px "Lato",sans-serif;letter-spacing:3px;text-align:center;margin-top:3px}
</style>
</head>
<body>

<!-- Top bar -->
<div class="abs topbar">
  <div class="social"><span></span><span></span><span></span><span></span><span></span></div>
  <div class="contact">
    <div><svg width="16" height="11" viewBox="0 0 16 11"><rect width="16" height="11" fill="#fff"/><path d="M0 0l8 6 8-6" stroke="#1d1d1d" stroke-width="1.5" fill="none"/></svg>info@tandrelbanners.com</div>
    <div><svg width="13" height="13" viewBox="0 0 24 24"><path fill="#fff" d="M6.6 10.8a15 15 0 006.6 6.6l2.2-2.2c.3-.3.7-.4 1-.2 1.1.4 2.3.6 3.6.6.6 0 1 .4 1 1V20c0 .6-.4 1-1 1A17 17 0 013 4c0-.6.4-1 1-1h3.5c.6 0 1 .4 1 1 0 1.3.2 2.5.6 3.6.1.3 0 .7-.2 1z"/></svg>123-456-7890</div>
  </div>
</div>

<!-- Header -->
<header class="abs header">
  <div class="brand">TANDREL<small>BANNERS</small></div>
  <nav class="nav"><a>PRODUCTS</a><a>GET A QUOTE</a><a>CONTACT US</a></nav>
</header>

<!-- Hero -->
<section class="abs hero" role="img" aria-label="Slideshow photo of printed banners laid out on a workshop floor">
  <div class="abs hero-shade"></div>
  <h1>We Are A New Australian Firm Which Will Sell Large Format Printed Banners And Other Signage Material</h1>
  <div class="cta">CONACT NOW !</div>
  <div class="dots"><span></span><span></span><span></span><span></span></div>
  <div class="bubble" role="img" aria-label="Photo of printed work in production" style="left:660px;top:30px;width:215px;height:215px;background:linear-gradient(135deg,#6d5a4a,#b89a7a)"></div>
  <div class="bubble" role="img" aria-label="Photo of a large printed store banner" style="left:880px;top:14px;width:215px;height:215px;background:linear-gradient(135deg,#3b6fb6,#e4e4e4)"></div>
  <div class="bubble" role="img" aria-label="Photo of printed flag banners" style="left:660px;top:215px;width:215px;height:215px;background:linear-gradient(135deg,#b43a2c,#e6c24a)"></div>
  <div class="bubble" role="img" aria-label="Photo of a large outdoor event banner" style="left:880px;top:215px;width:215px;height:215px;background:linear-gradient(135deg,#c22b22,#d8a640)"></div>
  <div class="bubble-badge">TANDREL</div>
</section>

<!-- Products -->
<h2 class="section-title" style="top:588px">OUR PRODUCTS</h2>
<div class="tile" role="img" aria-label="Banners and fabrics photo" style="left:98px;top:663px;background:linear-gradient(135deg,#4a3a2e,#8a6f52)">BANNERS &amp; FABRICS</div>
<div class="tile" role="img" aria-label="Boards and signs photo" style="left:450px;top:663px;background:linear-gradient(135deg,#5d4a4a,#9a8686)">BOARDS &amp; SIGNS</div>
<div class="tile" role="img" aria-label="Flags and point of sale photo" style="left:800px;top:663px;background:linear-gradient(135deg,#3e5a56,#9aa89a)">FLAGS &amp; POS</div>
<div class="tile" role="img" aria-label="Self adhesive vinyls photo" style="left:98px;top:903px;background:linear-gradient(135deg,#4a5a2a,#c89a3a)">SELF ADHESIVE VINYLS</div>
<div class="tile" role="img" aria-label="Pull up banners photo" style="left:450px;top:903px;background:linear-gradient(135deg,#4a4a4e,#8e8c8a)">PULL UP BANNERS</div>
<div class="tile" role="img" aria-label="Posters photo" style="left:800px;top:903px;background:linear-gradient(135deg,#5a5652,#a9a39b)">POSTERS</div>

<!-- Our difference -->
<section class="abs difference">
  <h2 class="section-title" style="top:36px">OUR DIFFERENCE</h2>
  <div class="feature" style="left:109px;top:128px">
    <div class="icon"><svg width="50" height="50" viewBox="0 0 50 50"><circle cx="20" cy="20" r="12" stroke="#fff" stroke-width="5" fill="none"/><path d="M29 29l14 14" stroke="#fff" stroke-width="7" stroke-linecap="round"/></svg></div>
    <h3>Attention To Detail</h3>
    <p>Lorem ipsum dolor sit amet, consectetur adipiscing elit. Aenean et dignissim sem, interdum risus.</p>
  </div>
  <div class="feature" style="left:367px;top:128px">
    <div class="icon"><svg width="50" height="50" viewBox="0 0 50 50"><circle cx="25" cy="25" r="15" stroke="#fff" stroke-width="4" fill="none"/><circle cx="25" cy="25" r="6" fill="#fff"/><path d="M25 3v10M25 37v10M3 25h10M37 25h10" stroke="#fff" stroke-width="4"/></svg></div>
    <h3>FAST AND FLEXIBLE</h3>
    <p>Lorem ipsum dolor sit amet, consectetur adipiscing elit. Aenean et dignissim sem, interdum risus.</p>
  </div>
  <div class="feature" style="left:607px;top:128px">
    <div class="icon"><svg width="50" height="50" viewBox="0 0 50 50"><path d="M8 26l11 11 23-24" stroke="#fff" stroke-width="7" fill="none" stroke-linecap="round" stroke-linejoin="round"/></svg></div>
    <h3>SECURE DELIVERY</h3>
    <p>Lorem ipsum dolor sit amet, consectetur adipiscing elit. Aenean et dignissim sem, interdum risus.</p>
  </div>
  <div class="feature" style="left:867px;top:128px">
    <div class="icon"><svg width="50" height="50" viewBox="0 0 50 50"><path d="M6 24L24 6h18v18L24 42z" fill="#fff"/><circle cx="34" cy="14" r="4" fill="#1e6fd1"/></svg></div>
    <h3>NICE PRICES</h3>
    <p>Lorem ipsum dolor sit amet, consectetur adipiscing elit. Aenean et dignissim sem, interdum risus.</p>
  </div>
</section>

<!-- About -->
<h2 class="about-title">ABOUT <b>TANDREL</b> BANNERS</h2>
<div class="abs about-body">
  <h4>OUR LITTLE BUSINESS</h4>
  <p>Lorem ipsum dolor sit amet, consectetur adipiscing elit. Aenean et dignissim sem, interdum risus. Vestibulum consectetur nisi mollis diam pulvinar adipiscing. Vestibulum ut urna nec nibh adipiscing facilisis. Etiam auctor porta lacus ac luctus. Praesent ac libero fermentum, rhoncus magna a, dapibus mauris. Nam ut auctor justo. Sed ante odio, luctus quis neque nec, adipiscing eleifend arcu. Integer nunc turpis, porttitor at lorem ut. Quisque hendrerit Lorem ipsum dolor sit amet, consectetur adipiscing elit. Aenean et dignissim sem, interdum risus. Vestibulum consectetur nisi mollis diam pulvinar adipiscing. Vestibulum ut urna nec nibh adipiscing facilisis. Etiam auctor porta lacus ac libero fermentum, rhoncus magna a, dapibus mauris.</p>
  <p>Lorem ipsum dolor sit amet, consectetur adipiscing elit. Aenean et dignissim sem, interdum risus. Vestibulum consectetur nisi mollis diam pulvinar adipiscing. Vestibulum ut urna nec nibh adipiscing facilisis. Etiam auctor porta lacus ac luctus. Praesent ac libero fermentum, rhoncus magna a, dapibus mauris.</p>
</div>
<div class="abs" role="img" aria-label="Photo of a printer operator at a large format printer" style="left:839px;top:1687px;width:261px;height:128px;background:linear-gradient(135deg,#c9ced6,#7b8796)"></div>
<div class="abs" role="img" aria-label="Photo of the business team" style="left:839px;top:1831px;width:261px;height:128px;background:linear-gradient(135deg,#d8dde2,#3d4048)"></div>

<!-- Latest work -->
<section class="abs work">
  <h2 class="section-title" style="top:40px">OUR LATEST WORK</h2>
  <div class="cell" role="img" aria-label="Printed wall signage" style="left:0;top:114px;width:195px;height:126px;background:linear-gradient(135deg,#d7d2c6,#6d9ab0)"></div>
  <div class="cell" role="img" aria-label="Pull up banner display" style="left:0;top:244px;width:195px;height:126px;background:linear-gradient(135deg,#e0b93a,#3a74c2)"></div>
  <div class="cell" role="img" aria-label="Row of pull up banners" style="left:0;top:374px;width:195px;height:156px;background:linear-gradient(135deg,#c9d46a,#e8e2d2)"></div>
  <div class="cell" role="img" aria-label="Hands holding printed material" style="left:197px;top:114px;width:195px;height:190px;background:linear-gradient(135deg,#d9d9d9,#4d6a8a)"></div>
  <div class="cell" role="img" aria-label="Event backdrop print" style="left:197px;top:308px;width:195px;height:222px;background:linear-gradient(135deg,#c8b8a8,#8a5a4a)"></div>
  <div class="cell" role="img" aria-label="Exhibition stand banners" style="left:394px;top:114px;width:194px;height:236px;background:linear-gradient(135deg,#bfbfbf,#2c4a6a)"></div>
  <div class="cell" role="img" aria-label="Infographic style print" style="left:394px;top:354px;width:194px;height:176px;background:linear-gradient(135deg,#e07a4a,#3aa0a0)"></div>
  <div class="cell" role="img" aria-label="Brochure print sample" style="left:590px;top:114px;width:217px;height:136px;background:linear-gradient(135deg,#3a3a3a,#c24a4a)"></div>
  <div class="cell" role="img" aria-label="Poster print sample" style="left:590px;top:254px;width:217px;height:276px;background:linear-gradient(135deg,#555,#a02a2a)"></div>
  <div class="cell cell-label" style="left:590px;top:334px;width:217px;height:196px">LOREM IPSUM<br>DOLOR SIT AMET</div>
  <div class="cell" role="img" aria-label="Typographic poster" style="left:809px;top:114px;width:195px;height:208px;background:linear-gradient(135deg,#eeeeee,#c62a2a)"></div>
  <div class="cell" role="img" aria-label="Flags on display" style="left:809px;top:326px;width:195px;height:204px;background:linear-gradient(135deg,#e6b84a,#c63a3a)"></div>
  <div class="cell" role="img" aria-label="Outdoor signage boards" style="left:1006px;top:114px;width:194px;height:126px;background:linear-gradient(135deg,#e0e0e0,#2a3a4a)"></div>
  <div class="cell" role="img" aria-label="Promotional sale signs" style="left:1006px;top:244px;width:194px;height:126px;background:linear-gradient(135deg,#f0e0d0,#d02a3a)"></div>
  <div class="cell" role="img" aria-label="Printed flyers" style="left:1006px;top:374px;width:194px;height:156px;background:linear-gradient(135deg,#e8efe8,#3a9a7a)"></div>
</section>

<!-- Process -->
<h2 class="section-title" style="top:2570px">OUR PROCESS</h2>
<div class="step" style="left:180px;top:2653px">
  <div class="ring"><svg width="50" height="50" viewBox="0 0 50 50"><rect x="6" y="10" width="30" height="30" stroke="#fff" stroke-width="4" fill="none"/><path d="M18 25h26M36 17l8 8-8 8" stroke="#fff" stroke-width="4" fill="none"/></svg></div>
  <p>LOREM IPSUM SIT DOLOR</p>
</div>
<div class="connector" style="left:388px;top:2714px"><span style="width:8px;height:8px"></span><span style="width:12px;height:12px"></span><span style="width:18px;height:18px"></span><span style="width:20px;height:20px"></span></div>
<div class="step" style="left:480px;top:2653px">
  <div class="ring"><svg width="50" height="50" viewBox="0 0 50 50"><rect x="10" y="8" width="30" height="36" rx="2" stroke="#fff" stroke-width="4" fill="none"/><rect x="18" y="4" width="14" height="8" fill="#fff"/><path d="M17 22h16M17 29h16M17 36h10" stroke="#fff" stroke-width="3"/></svg></div>
  <p>LOREM IPSUM SIT DOLOR</p>
</div>
<div class="connector" style="left:700px;top:2714px"><span style="width:8px;height:8px"></span><span style="width:12px;height:12px"></span><span style="width:18px;height:18px"></span><span style="width:20px;height:20px"></span></div>
<div class="step" style="left:790px;top:2653px">
  <div class="ring"><svg width="50" height="50" viewBox="0 0 50 50"><path d="M30 8H10v34h24V32" stroke="#fff" stroke-width="4" fill="none"/><path d="M20 24h24M36 16l8 8-8 8" stroke="#fff" stroke-width="4" fill="none"/></svg></div>
  <p>LOREM IPSUM SIT DOLOR</p>
</div>

<!-- Quote -->
<section class="abs quote">
  <h2>GET A QUOTE</h2>
  <div class="field" style="left:169px;top:119px;width:215px;height:30px">Name</div>
  <div class="field" style="left:398px;top:119px;width:215px;height:30px">Email</div>
  <div class="field" style="left:169px;top:158px;width:215px;height:30px">Phone Number</div>
  <div class="field" style="left:398px;top:158px;width:215px;height:30px">Enquiry Type<svg style="position:absolute;right:8px;top:11px" width="10" height="7" viewBox="0 0 10 7"><path d="M1 1l4 4 4-4" stroke="#888" stroke-width="1.5" fill="none"/></svg></div>
  <div class="field" style="left:629px;top:119px;width:400px;height:69px">Your Message</div>
  <div class="submit">SUBMIT</div>
</section>

<!-- Footer -->
<footer class="abs footer">
  <div class="abs" style="left:98px;top:42px">
    <h5>QUICK LINKS</h5>
    <ul class="links"><li>HOME</li><li>PRODUCTS</li><li>GET A QUOTE</li><li>CONTACT US</li></ul>
  </div>
  <div class="abs" style="left:313px;top:42px;width:290px">
    <h5>CONTACT DETAILS</h5>
    <div class="c-row"><svg width="18" height="24" viewBox="0 0 18 24"><path d="M9 0a9 9 0 00-9 9c0 7 9 15 9 15s9-8 9-15a9 9 0 00-9-9z" fill="#fff"/><circle cx="9" cy="9" r="3.5" fill="#3b3b3b"/></svg><div>TANDREL BANNERS,<br>Lorem ipsum dolor sit amet, conser</div></div>
    <div class="c-row"><svg width="18" height="18" viewBox="0 0 24 24"><path fill="#fff" d="M6.6 10.8a15 15 0 006.6 6.6l2.2-2.2c.3-.3.7-.4 1-.2 1.1.4 2.3.6 3.6.6.6 0 1 .4 1 1V20c0 .6-.4 1-1 1A17 17 0 013 4c0-.6.4-1 1-1h3.5c.6 0 1 .4 1 1 0 1.3.2 2.5.6 3.6.1.3 0 .7-.2 1z"/></svg><div><b style="color:#fff">123-456-7890</b><br><i>Available 24/7 - Call us any time.</i></div></div>
    <div class="c-row"><svg width="18" height="13" viewBox="0 0 16 11"><rect x=".5" y=".5" width="15" height="10" stroke="#fff" fill="none"/><path d="M.5.5l7.5 6 7.5-6" stroke="#fff" fill="none"/></svg><div><b style="color:#fff">info@tandrelbanners.com</b><br><i>Have a question? Let us help.</i></div></div>
  </div>
  <div class="abs" style="left:640px;top:42px">
    <h5>SUPPORT</h5>
    <div class="support-box"><svg width="34" height="28" viewBox="0 0 34 28"><path d="M3 2h22v14H12l-6 5v-5H3z" stroke="#fff" stroke-width="2.5" fill="none"/><path d="M28 9h4v13h-3v4l-5-4H13" stroke="#fff" stroke-width="2.5" fill="none"/></svg><div><b>Live Chat</b><i>Online Support</i></div></div>
    <div class="support-box" style="margin-top:10px"><svg width="34" height="34" viewBox="0 0 34 34"><path d="M10 11a7 7 0 1111 6c-3 2-4 3-4 7" stroke="#fff" stroke-width="4" fill="none"/><circle cx="17" cy="30" r="2.5" fill="#fff"/></svg><div><b>Help</b><i>Find your answers.</i></div></div>
  </div>
  <div class="foot-brand">TANDREL<small>BANNERS</small></div>
  <div class="abs social" style="left:903px;top:122px;position:absolute"><span style="background:#fff"></span><span style="background:#fff"></span><span style="background:#fff"></span><span style="background:#fff"></span><span style="background:#fff"></span></div>
  <div class="abs" style="left:903px;top:170px;font:700 11.5px/1.6 'Open Sans',sans-serif;color:#fff">© 2016 TANDREL BANNERS.<br>ALL RIGHTS RESERVED.</div>
</footer>

</body>
</html>
```